"Beyond Marrow Cay" Fictional Book Cover

BEYOND MARROW CAY
By: Dale Pruitt

Here's the intro .

"It had been nearly forty years since Ted Larraby last went to the island from where he was raised. Three months earlier he never would have thought about ever coming back. But life is weird. Things happen quickly and plans change, especially when your very life is at stake. The reason he was going back wasn’t to see old friends...no, no, no. They’re all dead. Of all the kids he grew up with on the island who moved off, he’s the only one still alive. Why?"

Pretty much all just a Lumeno book, by the way.

Target Market(s)

fiction readers

Requirements
Must have
• Somewhat of a dark, mysterious cover is what I'd like to see. Use your imagination. I've never written a fiction book before so I'm very open to ideas

Needs to have my name, DALE PRUITT at the bottom. like my other books, all of which are non-fiction
Nice to have
• Mysterious is what I'm looking for. NOT A HORROR story though. More a guy who left the island years ago, but is being called back to escape the rat race of modern, consumerist culture.

Please remember this NEEDS to jump out as a thumbnail on Bookvale as people are browsing. Mainly the WORDS need to stick out. Lighter words on a say a blue background.

If you want to try to use the attached pic, or something like this, to reflect an island in the cover, that'd be good.

I've also uploaded a couple images I purchased from Pixelcrate, hopefully you can make something work with these.

```html
<!DOCTYPE html>
<html lang="en">
<head>
<meta charset="utf-8">
<title>Beyond Marrow Cay — Dale Pruitt</title>
<link href="https://fonts.googleapis.com/css2?family=Yellowtail&family=Playfair+Display:wght@800;900&display=swap" rel="stylesheet">
<style>
  :root {
    --page-bg: #ffffff;
    --sky-top: #573f70;
    --sky-mid: #8a6277;
    --sky-glow: #d49c78;
    --horizon: #e6b58c;
    --treeline: #3b3232;
    --pier: #6a4b4c;
    --water: #2f2d3d;
    --water-deep: #22222f;
    --title-ink: #ffffff;
    --title-shadow: #3a2030;
  }
  * { margin: 0; padding: 0; box-sizing: border-box; }
  html, body {
    width: 720px;
    height: 1200px;
    overflow: hidden;
    background: var(--page-bg);
  }
  .book-cover {
    position: absolute;
    left: 20px;
    top: 97px;
    width: 680px;
    height: 1006px;
    overflow: hidden;
    box-shadow: 6px 8px 14px rgba(0,0,0,0.35);
  }
  .cover-photo {
    position: absolute;
    inset: 0;
    background: linear-gradient(to bottom,
      var(--sky-top) 0%,
      var(--sky-mid) 24%,
      var(--sky-glow) 40%,
      var(--horizon) 50%,
      var(--treeline) 53%,
      var(--pier) 62%,
      var(--pier) 70%,
      var(--water) 76%,
      var(--water-deep) 100%);
  }
  .title-script {
    position: absolute;
    top: 95px;
    width: 100%;
    text-align: center;
    font-family: "Yellowtail", cursive;
    font-size: 108px;
    line-height: 1;
    color: var(--title-ink);
    text-shadow: 3px 3px 0 var(--title-shadow);
  }
  .title-caps {
    position: absolute;
    top: 228px;
    width: 100%;
    text-align: center;
    font-family: "Playfair Display", serif;
    font-weight: 900;
    font-size: 82px;
    letter-spacing: 1px;
    line-height: 1;
    color: var(--title-ink);
    text-shadow: 3px 3px 0 var(--title-shadow);
  }
  .author-name {
    position: absolute;
    top: 888px;
    width: 100%;
    text-align: center;
    font-family: "Playfair Display", serif;
    font-weight: 800;
    font-size: 44px;
    letter-spacing: 1px;
    color: var(--title-ink);
  }
</style>
</head>
<body>
  <main class="book-cover">
    <div class="cover-photo" role="img" aria-label="Sepia-tinted photo of an island ferry pier with trees and houses under a purple-to-peach dusk sky over dark water"></div>
    <h1 class="book-title">
      <span class="title-script">Beyond</span>
      <span class="title-caps">MARROW CAY</span>
    </h1>
    <p class="author-name">DALE PRUITT</p>
  </main>
</body>
</html>
```